Regional Showdown Flyer for Holiday Program

Need a one page flyer, can be back to front or one page, ensuring you can fit all information, colourful, aimed at a market of 8-13 year old boys and girls.
The flyer needs to be noticed, needs to have certain information on it and needs to be Autralian Rule Football orientated.
Have uploaded file so you can understand the style (not content), style of flyer I am looking at getting submitted.

Target Market(s)

8-13 year old boys and girls and their parents.

Requirements
Must have
• Regional Showdown Event
• Price for Regional Showdown Day will be $85
• Strictly Limited Places, only the best footballers should enter this challenge
• Inaugural event, be the first Regional Showdown Winner for your age!
• Do you love a challenge! Put yourself to the test!
• Are you up to it - Water Slide Goal Kicking Contest! The fastest kick in the West (tested by our very own speed gun)! Can you survive the Footy Titan Trail or Last One Standing Goal Kicking! These challenges are crazy are super fun!
• If you think you can deliver on the big stage then this is for YOU!
• All District age winners will receive prizes, awards and the adulation from all their peers!
• Year's 3-5 from 9am to 12pm
• Year's 6-8 from 1-4pm
• All challengers compete against their own age
• Lunch Provided
• Monday 16th April - Upper Tarrowby Regional Showdown Day at Tarrowby Oval
• Tuesday 17th April - North Tarrowby Regional Showdown Day at Kilmorna Reserve
• Wednesday 18th April - Yarlo Regional Showdown Day - Dunhaven Football Club
• Every Challenge Participant receives a District Football!
• Need to put all 3 District Football Logos on the bottom of the flyer, logos attached at bottom.
Nice to have
• Plenty of colour, if you can fit all information on one page that would be fine
Should not have
• Dull, boring, any footballs should be Aussie Rules footballs not NFL or soccer

```html
<!DOCTYPE html>
<html lang="en">
<head>
<meta charset="utf-8">
<title>Regional Showdown Event Flyer</title>
<link href="https://fonts.googleapis.com/css2?family=Alfa+Slab+One&family=Oswald:wght@500;600;700&family=Lato:wght@400;700&display=swap" rel="stylesheet">
<style>
:root{
  --navy:#163b6b;
  --navy-band:#143a67;
  --red:#e5202a;
  --blue:#2a9fd8;
  --grey:#d3d5d8;
  --teal:#2fb9a4;
  --teal-dot:#8fdcd0;
  --ink:#1d1d1f;
  --white:#ffffff;
  --backdrop:#3e4a52;
}
*{box-sizing:border-box;margin:0;padding:0}
html,body{width:1200px;height:1200px;overflow:hidden}
body{background:var(--backdrop);position:relative;font-family:"Lato",sans-serif}
.flyer{position:absolute;left:160px;top:30px;width:880px;height:1140px;background:var(--white);overflow:hidden}
.hero-art{position:absolute;left:0;top:0;width:880px;height:620px;
  background:
    radial-gradient(ellipse 300px 230px at 440px 380px,rgba(238,70,60,.85) 0,rgba(243,150,50,.6) 45%,rgba(247,227,58,0) 80%),
    linear-gradient(120deg,#c23fb3 0%,#ee4fa6 35%,#f46f8f 55%,#e93fb3 80%,#f6c6e8 100%);}
.swoosh{position:absolute;left:0;top:0;width:880px;height:620px}
.title{position:absolute;left:139px;top:41px;width:601px;height:109px;background:var(--navy);border-radius:16px;
  display:flex;align-items:center;justify-content:center;border:4px solid var(--white)}
.title span{font-family:"Alfa Slab One",serif;font-size:92px;color:var(--white);letter-spacing:2px;line-height:1}
.subtitle{position:absolute;left:0;width:880px;top:156px;text-align:center;font-family:"Alfa Slab One",serif;
  font-size:46px;color:var(--red);letter-spacing:1px;-webkit-text-stroke:6px var(--white);paint-order:stroke fill}
.sessions{position:absolute;left:50px;top:562px;font-family:"Oswald",sans-serif;font-weight:600;color:var(--navy);text-transform:uppercase}
.sessions .row{font-size:33px;line-height:52px}
.sessions .row em{font-style:normal;color:var(--red)}
.sessions .note{font-size:25px;line-height:40px;margin-top:2px}
.price{position:absolute;left:630px;top:574px;width:222px;height:141px;border:2px dashed var(--teal-dot);border-radius:14px;text-align:center}
.price .amount{font-family:"Oswald",sans-serif;font-weight:700;font-size:56px;color:var(--red);line-height:62px;margin-top:2px}
.price .label{font-family:"Oswald",sans-serif;font-weight:700;font-size:44px;color:var(--ink);line-height:44px}
.price .day{font-family:Arial,sans-serif;font-weight:700;font-size:13.5px;color:var(--ink);margin-top:4px}
.dots{position:absolute;left:0;width:880px;height:8px}
.dots.top{top:730px}
.dots.bottom{top:938px}
.band{position:absolute;left:0;top:741px;width:880px;height:191px;background:var(--navy-band);padding:14px 40px 0 38px}
.band ul{list-style:none}
.band li{position:relative;padding-left:33px;color:var(--white);font-size:14px;line-height:17.5px;margin-bottom:8.5px}
.band li svg{position:absolute;left:0;top:2px;width:18px;height:13px}
.schedule{position:absolute;left:39px;top:958px;font-size:16.5px;color:var(--ink)}
.schedule .day{margin-bottom:7px;line-height:20.5px}
.schedule .date{color:var(--navy);font-weight:700}
.schedule .lunch{color:var(--red);font-weight:700;line-height:20.5px}
.giveaway{position:absolute;left:512px;top:957px;width:322px;height:84px;background:var(--teal);border-radius:10px;
  box-shadow:0 3px 0 #1f8f7e;color:var(--white);font-weight:700;font-size:21.5px;line-height:28px;padding:13px 0 0 18px}
.districts{position:absolute;left:512px;top:1068px;width:330px;display:flex;justify-content:space-between;align-items:center}
.district{display:flex;align-items:center;gap:5px;font-family:"Lato",sans-serif;font-weight:700;font-size:11px;color:var(--navy);line-height:12px}
.district i{display:block;width:22px;height:22px;border-radius:50%;background:var(--teal)}
</style>
</head>
<body>
<main class="flyer">
  <div class="hero-art" role="img" aria-label="Aussie Rules football bursting through a splash of pink, purple, yellow and blue paint"></div>
  <svg class="swoosh" viewBox="0 0 880 620" aria-hidden="true">
    <path d="M0,330 C110,420 250,500 440,515 C630,520 770,470 880,395 L880,620 L0,620 Z" fill="var(--blue)"/>
    <path d="M0,520 C140,500 270,505 440,512 C620,514 760,480 880,430 L880,620 L0,620 Z" fill="var(--grey)"/>
    <path d="M0,575 C110,525 250,522 440,530 C640,536 770,520 880,527 L880,620 L0,620 Z" fill="var(--white)"/>
  </svg>

  <h1 class="title"><span>REGIONAL</span></h1>
  <h2 class="subtitle">SHOWDOWN EVENT</h2>

  <section class="sessions">
    <p class="row">Year's <em>3-5</em> from <em>9am to 12pm</em></p>
    <p class="row">Year's <em>6-8</em> from <em>1-4pm</em></p>
    <p class="note">All challengers compete against their own age</p>
  </section>

  <aside class="price">
    <p class="amount">$85</p>
    <p class="label">PRICE FOR</p>
    <p class="day">REGIONAL SHOWDOWN DAY</p>
  </aside>

  <svg class="dots top" viewBox="0 0 880 8" aria-hidden="true"><line x1="4" y1="4" x2="878" y2="4" stroke="var(--teal-dot)" stroke-width="5" stroke-linecap="round" stroke-dasharray="0 9.5"/></svg>

  <section class="band">
    <ul>
      <li><svg viewBox="0 0 18 13"><path d="M0,0 L18,6.5 L0,13 L5,6.5 Z" fill="#fff"/></svg>Strictly Limited Places, only the best footballers should enter this challenge</li>
      <li><svg viewBox="0 0 18 13"><path d="M0,0 L18,6.5 L0,13 L5,6.5 Z" fill="#fff"/></svg>Inaugural event, be the first Regional Showdown Winner for your age!</li>
      <li><svg viewBox="0 0 18 13"><path d="M0,0 L18,6.5 L0,13 L5,6.5 Z" fill="#fff"/></svg>Do you love a challenge! Put yourself to the test!</li>
      <li><svg viewBox="0 0 18 13"><path d="M0,0 L18,6.5 L0,13 L5,6.5 Z" fill="#fff"/></svg>Are you up to it - Water Slide Goal Kicking Contest! The fastest kick in the West (tested by our very own speed gun)! Can you survive the Footy Titan Trail or Last One Standing Goal Kicking! These challenges are crazy are super fun!</li>
      <li><svg viewBox="0 0 18 13"><path d="M0,0 L18,6.5 L0,13 L5,6.5 Z" fill="#fff"/></svg>If you think you can deliver on the big stage then this is for YOU!</li>
      <li><svg viewBox="0 0 18 13"><path d="M0,0 L18,6.5 L0,13 L5,6.5 Z" fill="#fff"/></svg>All District age winners will receive prizes, awards and the adulation from all their peers!</li>
    </ul>
  </section>

  <svg class="dots bottom" viewBox="0 0 880 8" aria-hidden="true"><line x1="4" y1="4" x2="878" y2="4" stroke="var(--teal-dot)" stroke-width="5" stroke-linecap="round" stroke-dasharray="0 9.5"/></svg>

  <section class="schedule">
    <p class="day"><span class="date">Monday 16th April -</span><br>Upper Tarrowby Regional Showdown Day at Tarrowby Oval</p>
    <p class="day"><span class="date">Tuesday 17th April -</span><br>North Tarrowby Regional Showdown Day at Kilmorna Reserve</p>
    <p class="day"><span class="date">Wednesday 18th April -</span><br>Yarlo Regional Showdown Day - Dunhaven Football Club</p>
    <p class="lunch">Lunch Provided</p>
  </section>

  <div class="giveaway">Every Challenge Participant<br>receives a District Football!</div>

  <footer class="districts">
    <div class="district"><i></i><span>YARLO<br>DISTRICT</span></div>
    <div class="district"><i></i><span>STINGRAYS<br>DISTRICT</span></div>
    <div class="district"><i></i><span>KESTRELS<br>DISTRICT</span></div>
  </footer>
</main>
</body>
</html>
```